Business Card Project for Firm Deck Hoisting

Business name is "Firm Deck Hoisting" we are a scaffolding & rigging business specialising in local and remote work for:
- scaffolding (residential, commercial, industrial)
- rigging
-man material hoists
- swing stages
- labour hire

On the back of the card I would like FDH as the symbol / logo. I have attached the logos we have had created by sketch harbour. We would like to use bold colours – preferably as the same colour scheme as the logo.

Target Market(s)

Construction business

Industry/Entity Type

Construction

Contact Information for Business Card

name: Owen Pellew
Title: Director
Phone: 0491 572 864
Address: PO BOX 3251, Tarrowby SA 5271
Email: owen@firmdeckhoisting.com.au
Website: www.firmdeckhoisting.com.au

Font styles to use
Sans Serif

Requirements
Must have
• Must use existing logo & prefering using bold colours
Nice to have
• Would be nice to have a line of dot points in what we specialise in but not essential
• Would be nice to see some designs with a slogan but not essential
Should not have
• NA

```html
<!DOCTYPE html>
<html lang="en">
<head>
<meta charset="utf-8">
<title>Firm Deck Hoisting – Business Card</title>
<link rel="stylesheet" href="https://fonts.googleapis.com/css2?family=Arimo:wght@400;700&display=swap">
<style>
  :root {
    --backdrop: #2b2b2b;
    --card-white: #ffffff;
    --brand-blue: #1e74be;
    --ink: #1f1f1f;
    --ink-soft: #3a3a3a;
    --icon-bg: #1a1a1a;
  }
  * { box-sizing: border-box; margin: 0; padding: 0; }
  html, body {
    width: 1200px; height: 1000px; overflow: hidden;
    background: var(--backdrop);
    font-family: "Arimo", Arial, sans-serif;
  }
  .canvas {
    position: relative; width: 1200px; height: 1000px;
    display: flex; flex-direction: column; align-items: center; justify-content: center; gap: 60px;
  }
  .card {
    position: relative; width: 620px; height: 379px;
    box-shadow: 0 10px 30px rgba(0,0,0,.45);
  }
  .card--front { background: var(--card-white); }
  .card--back {
    background: var(--brand-blue);
    display: flex; align-items: center; justify-content: center;
  }

  .brand {
    position: absolute; right: 38px; top: 70px;
    display: flex; align-items: center; gap: 10px;
  }
  .brand__square { width: 14px; height: 14px; background: var(--brand-blue); }
  .brand__name { font-size: 26px; font-weight: 700; color: var(--ink); letter-spacing: .5px; }

  .divider {
    position: absolute; left: 0; right: 0; top: 182px; height: 6px;
    background: var(--brand-blue);
  }

  .person { position: absolute; left: 38px; top: 134px; }
  .person__name { font-size: 17px; font-weight: 700; color: var(--brand-blue); }
  .person__title { font-size: 15px; color: var(--ink-soft); margin-top: 2px; }

  .address {
    position: absolute; right: 38px; top: 212px; text-align: right;
    font-size: 14px; line-height: 20px; color: var(--ink-soft);
    font-style: normal;
  }
  .address .icon { margin: 0 0 12px auto; }

  .contacts {
    position: absolute; left: 38px; top: 272px; list-style: none;
    display: flex; flex-direction: column; gap: 9px;
  }
  .contacts li { display: flex; align-items: center; gap: 8px; font-size: 14px; color: var(--ink-soft); }

  .icon {
    width: 16px; height: 16px; background: var(--icon-bg); border-radius: 2px;
    display: flex; align-items: center; justify-content: center;
  }
  .icon svg { width: 10px; height: 10px; }

  .back__name { font-size: 72px; font-weight: 700; color: var(--card-white); letter-spacing: 4px; }
</style>
</head>
<body>
<main class="canvas">
  <section class="card card--front" aria-label="Business card front">
    <div class="brand">
      <span class="brand__square"></span>
      <span class="brand__name">Firm Deck Hoisting</span>
    </div>

    <div class="person">
      <p class="person__name">Owen Pellew</p>
      <p class="person__title">Director</p>
    </div>

    <div class="divider"></div>

    <address class="address">
      <span class="icon">
        <svg viewBox="0 0 10 10"><path fill="#fff" d="M5 0.5a3.2 3.2 0 0 0-3.2 3.2C1.8 6 5 9.5 5 9.5S8.2 6 8.2 3.7A3.2 3.2 0 0 0 5 0.5zm0 4.5a1.3 1.3 0 1 1 0-2.6 1.3 1.3 0 0 1 0 2.6z"/></svg>
      </span>
      PO BOX 3251,<br>Tarrowby SA 5271
    </address>

    <ul class="contacts">
      <li>
        <span class="icon"><svg viewBox="0 0 10 10"><path fill="#fff" d="M2.2 0.8l1.5 1.9-.9 1.1c.6 1.2 1.4 2 2.6 2.6l1.1-.9 1.9 1.5-.9 1.9C4.6 8.7 1.3 5.4.5 2.6z"/></svg></span>
        0491 572 864
      </li>
      <li>
        <span class="icon"><svg viewBox="0 0 10 10"><rect x="0.8" y="2" width="8.4" height="6" fill="none" stroke="#fff" stroke-width="1"/><path d="M0.8 2L5 5.5 9.2 2" fill="none" stroke="#fff" stroke-width="1"/></svg></span>
        owen@firmdeckhoisting.com.au
      </li>
      <li>
        <span class="icon"><svg viewBox="0 0 10 10"><circle cx="5" cy="5" r="4" fill="none" stroke="#fff" stroke-width="1"/><ellipse cx="5" cy="5" rx="1.7" ry="4" fill="none" stroke="#fff" stroke-width=".8"/><path d="M1 5h8" stroke="#fff" stroke-width=".8"/></svg></span>
        www.firmdeckhoisting.com.au
      </li>
    </ul>
  </section>

  <section class="card card--back" aria-label="Business card back">
    <span class="back__name">FDH</span>
  </section>
</main>
</body>
</html>
```